Poster design for a company operating care homes in the UK showcasing our core values

We need a poster to display in our care homes showcasing our new core values:

Purpose
We are driven by a clear understanding of why we do what we do: to enrich lives, honour legacies and make a meaningful difference every day, for our residents, their families, our colleagues and our community.

Excellence
We hold ourselves to the highest standards, delivering exceptional care and creating an environment where both residents and staff can thrive.

Openness
We build trust through honest, respectful communication, welcoming feedback, sharing ideas, and embracing change as a path to continuous growth.

Passion
We are passionate about delivering exceptional care. We take pride in what we do and in making a real difference in people’s lives.

Learning
We are committed to personal and professional growth; empowering each other through ongoing development, reflection, and shared knowledge.

Empathy
We actively listen and seek to understand before being understood, recognising the unique stories, feelings, and needs of others.

I have attached a small graphic that we would like you try to incorporate, in addition to our company logo. Please theme the rest of the poster around our company colours.

```html
<!DOCTYPE html>
<html lang="en">
<head>
<meta charset="utf-8">
<title>Meridian – Our Core Values</title>
<link href="https://fonts.googleapis.com/css2?family=Mulish:wght@400;600;800&family=Nunito:wght@800;900&family=Bebas+Neue&display=swap" rel="stylesheet">
<style>
  :root{
    --navy:#2b3f62;
    --peach:#d9a27c;
    --paper:#f3f2ef;
    --stage:#e4e3e0;
    --blob:#d7dce1;
    --blob-soft:#ebe8e3;
    --text:#33425f;
    --frame:#ffffff;
  }
  *{box-sizing:border-box;margin:0;padding:0}
  html,body{width:1200px;height:1163px;overflow:hidden}
  body{background:var(--stage);font-family:"Mulish",sans-serif;color:var(--text)}
  .poster{position:absolute;left:220px;top:20px;width:760px;height:1123px;background:var(--paper);overflow:hidden}
  .blob{position:absolute;left:0;top:0}
  .brand{position:absolute;top:40px;left:0;width:100%;display:flex;justify-content:center;align-items:center;gap:12px}
  .brand-mark{width:20px;height:20px;border-radius:50%;background:var(--navy)}
  .brand-name{font-family:"Mulish",sans-serif;font-weight:800;font-size:42px;line-height:1;letter-spacing:1px;color:var(--navy)}
  .title{position:absolute;top:108px;width:100%;text-align:center;font-family:"Nunito",sans-serif;font-weight:900;font-size:58px;line-height:1.2;color:var(--peach)}
  .intro{position:absolute;top:188px;left:40px;width:680px;text-align:center;font-size:15.5px;line-height:1.45;color:var(--text)}
  .photo{position:absolute;background:var(--frame);padding:7px;box-shadow:0 3px 8px rgba(0,0,0,.18)}
  .photo .fill{width:100%;height:100%}
  .hex{position:absolute;width:120px;height:106px;clip-path:polygon(25% 0,75% 0,100% 50%,75% 100%,25% 100%,0 50%);display:flex;align-items:center;justify-content:center;font-family:"Bebas Neue",sans-serif}
  .hex .initial{font-size:40px;line-height:1}
  .hex .rest{font-size:16px;letter-spacing:.5px;margin-top:9px}
  .hex--peach{background:var(--peach);color:var(--navy)}
  .hex--navy{background:var(--navy);color:var(--peach)}
  .values{position:absolute;top:722px;left:50px;right:50px;display:grid;grid-template-columns:repeat(3,1fr);column-gap:30px;row-gap:16px}
  .value:nth-child(3n+1){transform:translateY(16px)}
  .value:nth-child(3n+2){transform:translateY(8px)}
  .value h2{font-family:"Mulish",sans-serif;font-weight:800;font-size:16px;line-height:1.3;color:var(--navy);margin-bottom:3px}
  .value p{font-size:13px;line-height:1.42;text-align:justify;hyphens:auto}
  .web{position:absolute;bottom:16px;width:100%;text-align:center;font-weight:600;font-size:14px;color:var(--navy)}
</style>
</head>
<body>
<main class="poster">
  <svg class="blob" width="760" height="1123" viewBox="0 0 760 1123" aria-hidden="true">
    <path d="M560 0 H760 V240 C720 250 690 200 680 150 C660 80 600 60 540 50 C520 30 530 5 560 0Z" fill="var(--blob)"/>
    <path d="M0 520 C40 500 70 540 60 600 C55 640 20 660 0 650Z" fill="var(--blob)"/>
    <path d="M100 700 C260 640 520 650 760 690 V1123 H0 V790 C30 760 60 730 100 700Z" fill="var(--blob-soft)"/>
  </svg>

  <header class="brand">
    <span class="brand-mark"></span>
    <span class="brand-name">MERIDIAN</span>
  </header>

  <h1 class="title">Our Core Values</h1>
  <p class="intro">At Meridian, in collaboration with our wider team, we have developed Core Values that reflect our shared priorities and define how we support and show up for one another every day.</p>

  <div class="photo" style="left:150px;top:272px;width:150px;height:160px;transform:rotate(2deg)"><div class="fill" role="img" aria-label="Resident smiling and playing with an orange balloon" style="background:linear-gradient(160deg,#8a6a52,#c9a88a)"></div></div>
  <div class="photo" style="left:322px;top:262px;width:168px;height:140px;transform:rotate(-2deg)"><div class="fill" role="img" aria-label="Carer in blue uniform helping a resident" style="background:linear-gradient(160deg,#4a6d9e,#b9a99a)"></div></div>
  <div class="photo" style="left:525px;top:256px;width:158px;height:158px;transform:rotate(-3deg)"><div class="fill" role="img" aria-label="Close view of an elderly person's hands" style="background:linear-gradient(160deg,#3f7470,#c49b86)"></div></div>
  <div class="photo" style="left:80px;top:420px;width:172px;height:150px;transform:rotate(-4deg)"><div class="fill" role="img" aria-label="Carer in a mask sitting with a resident in a lounge" style="background:linear-gradient(160deg,#6d5a52,#a7b4c9)"></div></div>
  <div class="photo" style="left:270px;top:405px;width:175px;height:150px;transform:rotate(-3deg)"><div class="fill" role="img" aria-label="Residents and staff sharing a meal at a table" style="background:linear-gradient(160deg,#8f6f5a,#9fb3c2)"></div></div>
  <div class="photo" style="left:462px;top:385px;width:165px;height:150px;transform:rotate(-4deg)"><div class="fill" role="img" aria-label="Smiling resident wearing glasses holding a carer's hand" style="background:linear-gradient(160deg,#7a6a66,#d2c4bd)"></div></div>

  <div class="hex hex--peach" style="left:85px;top:605px"><span class="initial">P</span><span class="rest">urpose</span></div>
  <div class="hex hex--navy" style="left:190px;top:570px"><span class="initial">E</span><span class="rest">xcellence</span></div>
  <div class="hex hex--peach" style="left:295px;top:600px"><span class="initial">O</span><span class="rest">penness</span></div>
  <div class="hex hex--navy" style="left:400px;top:565px"><span class="initial">P</span><span class="rest">assion</span></div>
  <div class="hex hex--peach" style="left:505px;top:595px"><span class="initial">L</span><span class="rest">earning</span></div>
  <div class="hex hex--navy" style="left:610px;top:560px"><span class="initial">E</span><span class="rest">mpathy</span></div>

  <div class="values">
    <section class="value"><h2>Purpose</h2><p>We are driven by a clear understanding of why we do what we do: to enrich lives, honour legacies and make a meaningful difference every day, for our residents, their families, our colleagues and our community.</p></section>
    <section class="value"><h2>Excellence</h2><p>We hold ourselves to the highest standards, delivering exceptional care and creating an environment where both residents and staff can thrive.</p></section>
    <section class="value"><h2>Openness</h2><p>We build trust through honest, respectful communication, welcoming feedback, sharing ideas, and embracing change as a path to continuous growth.</p></section>
    <section class="value"><h2>Passion</h2><p>We are passionate about delivering exceptional care. We take pride in what we do and in making a real difference in people’s lives.</p></section>
    <section class="value"><h2>Learning</h2><p>We are committed to personal and professional growth; empowering each other through ongoing development, reflection, and shared knowledge.</p></section>
    <section class="value"><h2>Empathy</h2><p>We actively listen and seek to understand before being understood, recognising the unique stories, feelings, and needs of others.</p></section>
  </div>

  <footer class="web">www.meridiancarehomes.co.uk</footer>
</main>
</body>
</html>
```